Technology Company Web Design Project

We are working with BrimCore. They are a technology company and in need of a new website design.
BrimCore helps companies control who (or what) can access which information inside their systems — and under what conditions. Think of them as the traffic controller for digital access and data permissions.
Instead of letting every app, employee, or AI bot freely connect to everything, GatewardIQ makes sure:
• Each one only gets access to what it actually needs.
• That access follows company rules automatically.
• Those rules are enforced the same way everywhere — across apps, servers, and even AI tools.
Some competitor sites to use for inspiration:
https://www.trovanexus.example/en/lp/ac/trovaspire.html
https://www.clearrulekeeper.example
https://www.vondix.example
Thank you for taking the time to consider designing a website for us. We are web developers based in Stockton and Los Angeles, CA, USA. Most of our projects go through the same process. Understanding this process may help you win a project with us. We custom-code all of our websites in-house. We don’t have any requirements as to what tools you use for your design, but we prefer Drafton files. For any design that we label as four-stars, we send it to the client for review. The client picks the final design they want us to use. Once we complete this process, we will continue to show additional clients all the four-star sites and purchase them later. Your designs will have multiple chances to sell. For better chances of success, we ask that you follow these guidelines.
IMAGES:
If you use any images or icons in the design, we ask that you have a link to the asset so we can purchase the image/icon. Most of the designs we submit do not have the customer’s images on them unless they have some great images. Be creative; show us the feeling you are trying to portray with your image choices. Use any royalty-free site you choose. We subscribe to Kelvaro and mainly use their images, but we can purchase images outside of Kelvaro.
PLEASE NOTE: we will not submit designs to clients with watermarks on the images.
FONTS:
We ask that you identify the fonts used in the design. This can be done in a message if you want. We typically use Quillny Fonts and Kelvaro Fonts.
CONTENT:
We're always open to different content and ideas. We often submit designs with stock images so the client can see our vision. We typically take pictures after the website launch to use their images with our vision. Lorem Ipsum is fine for paragraphs, but we ask that you write the headers in correct English. We want to be able to show the vision and identify the sections of the website.
INSPIRATION:
We typically add a couple of links in the brief of websites we like to help you get started in your design.
REVISIONS:
We do not often ask for revisions of the designs unless we see something in the design that may not appeal to the client. If there are slight changes that we want to make, we do that in the development process.
FEEDBACK:
We rarely give feedback on designs during the design process. We are working on many website projects and do not have the time to provide feedback. We usually respond if your request is well thought out and asks specific questions, but a note asking “feedback, please” usually goes unanswered.

```html
<!DOCTYPE html>
<html lang="en">
<head>
<meta charset="utf-8">
<title>BrimCore – GatewardIQ</title>
<link href="https://fonts.googleapis.com/css2?family=Lato:wght@400;700;900&display=swap" rel="stylesheet">
<style>
:root{
  --navy:#1b2f55;
  --deep:#08142e;
  --footer:#152a4f;
  --orange:#e06c25;
  --ink:#1d1d1d;
  --muted:#6b6b6b;
  --pale:#e2ecfb;
  --white:#ffffff;
}
*{box-sizing:border-box;margin:0;padding:0}
html,body{width:1200px;height:4360px;overflow:hidden}
body{position:relative;background:var(--white);font-family:'Lato',sans-serif;color:var(--ink)}
.abs{position:absolute}
a{color:inherit;text-decoration:none}
h1,h2,h3,h4{font-weight:400}

/* hero */
.hero{position:absolute;left:0;top:0;width:1200px;height:627px;background:radial-gradient(circle at 78% 40%,#16356b 0%,#0b1c3d 40%,var(--deep) 75%);border-bottom-right-radius:260px 300px;overflow:hidden}
.hero-art{position:absolute;left:640px;top:150px;width:560px;height:380px;background:radial-gradient(ellipse at 45% 45%,rgba(40,110,200,.55),rgba(10,30,70,0) 65%)}
.brand{position:absolute;left:112px;top:100px;font-weight:900;font-size:34px;letter-spacing:2px;color:var(--orange)}
.nav{position:absolute;top:58px;left:0;font-size:15px;color:var(--white)}
.nav a{position:absolute;white-space:nowrap}
.nav .active{color:var(--orange)}
.nav .active::after{content:"";position:absolute;left:0;right:0;top:26px;height:3px;background:var(--orange)}
.btn{display:inline-flex;align-items:center;justify-content:center;background:var(--orange);color:var(--white);font-weight:700;font-size:16px;border-radius:4px 14px 4px 14px}
.welcome{left:108px;top:240px;color:var(--white);font-size:24px;font-weight:700}
.hero-title{left:106px;top:275px;color:var(--white);font-size:70px;font-weight:900;letter-spacing:.5px}
.hero-sub{left:108px;top:372px;color:var(--white);font-size:33px}

/* pillars */
.pillar{position:absolute;top:537px;width:184px;height:184px;border-radius:50%;background:var(--white);text-align:center}
.pillar .ic{margin:42px auto 0;width:48px;height:48px}
.pillar p{font-size:19px;line-height:26px;margin-top:20px;color:var(--ink)}
.pillar.on p{color:var(--orange);font-weight:700}

/* headings */
.heading{position:absolute;left:0;width:1200px;text-align:center;font-size:43px;font-weight:400;color:var(--ink)}
.heading b{color:var(--navy);font-weight:700}
.rule{position:absolute;height:3px;width:74px;background:var(--orange)}
.rule::after{content:"";position:absolute;right:-4px;top:-4px;width:11px;height:11px;border-radius:50%;background:var(--orange)}

/* about */
.photo{position:absolute}
.about-text{left:643px;width:450px;font-size:13.5px;line-height:29.5px;color:#555;text-align:justify}

/* platform */
.band{position:absolute;left:0;width:1200px;background:var(--pale)}
.card{position:absolute;top:1510px;width:233px;height:241px;background:var(--white);border:2px solid #d6d6d6;border-radius:4px;text-align:center;padding-top:68px}
.card h3{font-size:19px;font-weight:700;line-height:25px;color:var(--navy)}
.card p{font-size:13px;line-height:25px;color:#777;margin-top:20px;padding:0 38px}
.card.on{background:var(--orange);border-color:var(--orange)}
.card.on h3,.card.on p{color:var(--white)}
.card .badge{position:absolute;left:50%;top:-24px;margin-left:-35px;width:70px;height:70px;border-radius:50%;background:var(--navy);border:3px solid var(--white);display:flex;align-items:center;justify-content:center}
.card.on .badge{background:var(--orange)}

/* partners */
.partner{position:absolute;top:2090px;width:240px;text-align:center;font-size:30px;font-weight:700;color:var(--navy)}

/* features */
.feat{position:absolute;left:110px;width:420px;font-size:12.5px;line-height:24px;color:#555;padding-left:42px}
.feat::before{content:"";position:absolute;left:0;top:3px;width:19px;height:19px;border-radius:50%;background:var(--orange)}
.feat::after{content:"";position:absolute;left:5px;top:9px;width:6px;height:6px;border-top:2px solid #fff;border-right:2px solid #fff;transform:rotate(45deg)}

/* capabilities */
.cap-ic{position:absolute;width:70px;height:70px;border-radius:50%;display:flex;align-items:center;justify-content:center}
.cap-ic.l{background:var(--navy)}
.cap-ic.r{background:var(--orange)}
.cap-label{position:absolute;font-size:19px;font-weight:700;color:var(--ink);white-space:nowrap}

/* resources */
.post{position:absolute;top:3440px;width:314px;height:369px;background:var(--white);box-shadow:0 4px 14px rgba(0,0,0,.1)}
.post .thumb{height:212px;background:radial-gradient(circle at 50% 50%,#1f5e9a,#0a1a33 75%)}
.post .tag{margin:18px 14px 0;font-size:15px;font-weight:700;color:var(--orange)}
.post h4{margin:10px 14px 0;font-size:17.5px;font-weight:400;line-height:26px;color:var(--ink)}
.post .meta{margin:12px 14px 0;font-size:12px;color:#777;display:flex;gap:34px}

/* footer */
.footer{position:absolute;left:0;top:3979px;width:1200px;height:381px;background:var(--footer);border-top-left-radius:110px}
.f-head{position:absolute;font-size:22px;font-weight:700;color:var(--white)}
.f-link{position:absolute;left:123px;font-size:14.5px;color:var(--white)}
.f-contact{position:absolute;left:904px;font-size:14px;color:var(--white)}
.social{position:absolute;top:4256px;width:30px;height:30px;border-radius:50%;background:var(--white)}
.social.on{background:var(--orange)}
.f-brand{position:absolute;left:400px;top:4165px;width:400px;text-align:center;font-size:54px;font-weight:900;letter-spacing:4px;color:var(--white)}
.f-rule{position:absolute;left:108px;top:4320px;width:984px;height:1px;background:rgba(255,255,255,.5)}
.copy{position:absolute;left:0;top:4331px;width:1200px;text-align:center;font-size:13px;color:var(--white)}
</style>
</head>
<body>

<header class="hero">
  <div class="hero-art" role="img" aria-label="Glowing digital shield with padlock over a circuit board, with user and AI chip icons"></div>
  <div class="brand">BRIMCORE</div>
  <nav class="nav">
    <a class="active" style="left:406px">Home</a>
    <a style="left:496px">Product</a>
    <a style="left:592px">Solutions</a>
    <a style="left:699px">Resources</a>
    <a style="left:811px">Company</a>
  </nav>
  <a class="btn abs" style="left:948px;top:37px;width:139px;height:48px;font-weight:400">GET A DEMO</a>
  <div class="abs welcome">Welcome To BRIMCORE</div>
  <h1 class="abs hero-title">GatewardIQ</h1>
  <div class="abs hero-sub">The traffic controller for your data</div>
  <a class="btn abs" style="left:112px;top:440px;width:139px;height:48px;font-weight:400">GET STARTED</a>
</header>

<div class="pillar" style="left:297px">
  <svg class="ic" viewBox="0 0 48 48"><path d="M24 3l17 7v12c0 11-7 19-17 23C14 41 7 33 7 22V10z" fill="#6b6b6b"/><rect x="16" y="21" width="16" height="13" rx="2" fill="#fff"/><path d="M19 21v-4a5 5 0 0110 0v4" fill="none" stroke="#fff" stroke-width="2.5"/></svg>
  <p>Data Privacy</p>
</div>
<div class="pillar on" style="left:509px">
  <svg class="ic" viewBox="0 0 48 48"><circle cx="24" cy="24" r="21" fill="#e06c25"/><circle cx="24" cy="24" r="13" fill="none" stroke="#fff" stroke-width="3"/><path d="M18 24l5 5 8-9" fill="none" stroke="#fff" stroke-width="3"/></svg>
  <p>Trustworthy<br>Interactions</p>
</div>
<div class="pillar" style="left:718px">
  <svg class="ic" viewBox="0 0 48 48"><circle cx="24" cy="24" r="20" fill="#6b6b6b"/><path d="M17 18l-6 6 6 6M31 18l6 6-6 6M27 15l-6 18" fill="none" stroke="#fff" stroke-width="3"/></svg>
  <p style="margin-top:10px">Precision &amp;<br>Compliance</p>
</div>

<div class="photo" role="img" aria-label="Hand holding a tablet projecting a glowing VPN shield with padlock and network icons" style="left:110px;top:806px;width:445px;height:393px;background:radial-gradient(circle at 50% 45%,#3b8fe0,#0e2f66 55%,#081a3a)"></div>
<h2 class="abs" style="left:648px;top:795px;font-size:44px">About <b style="color:var(--navy)">Us</b></h2>
<div class="rule" style="left:643px;top:863px"></div>
<p class="abs about-text" style="top:888px">BrimCore helps companies control who (or what) can access which information inside their systems — and under what conditions. Think of them as the traffic controller for digital access and data permissions.</p>
<p class="abs about-text" style="top:987px">Lorem ipsum dolor sit amet, consectetur adipiscing elit, sed do eiusmod tempor incididunt ut labore et dolore magna aliqua. Ut enim ad minim veniam, quis nostrud exercitation ullamco laboris nisi ut aliquip ex ea commodo consequat. Duis aute irure dolor in reprehenderit in voluptate velit esse cillum dolore eu fugiat nulla pariatur.</p>
<a class="btn abs" style="left:643px;top:1148px;width:139px;height:48px;font-weight:400">READ MORE</a>

<section class="band" style="top:1317px;height:532px"></section>
<h2 class="heading" style="top:1380px">One Platform for <b>All Your Needs</b></h2>
<div class="rule" style="left:560px;top:1446px"></div>

<div class="card" style="left:112px">
  <div class="badge"><svg width="34" height="34" viewBox="0 0 34 34"><circle cx="17" cy="17" r="7" fill="none" stroke="#fff" stroke-width="3"/><circle cx="7" cy="10" r="3" fill="#fff"/><circle cx="27" cy="10" r="3" fill="#fff"/><circle cx="7" cy="25" r="3" fill="#fff"/><circle cx="27" cy="25" r="3" fill="#fff"/></svg></div>
  <h3>Workforce<br>Authorization</h3>
  <p>Duis aute irure dolor in reprehenderit in voluptate</p>
</div>
<div class="card on" style="left:357px">
  <div class="badge"><svg width="34" height="34" viewBox="0 0 34 34"><circle cx="17" cy="12" r="7" fill="#fff"/><path d="M5 31c0-7 5-11 12-11s12 4 12 11z" fill="#fff"/></svg></div>
  <h3>Customer<br>Authorization</h3>
  <p>Duis aute irure dolor in reprehenderit in voluptate</p>
</div>
<div class="card" style="left:604px">
  <div class="badge"><svg width="34" height="34" viewBox="0 0 34 34"><ellipse cx="14" cy="8" rx="9" ry="4" fill="#fff"/><rect x="5" y="11" width="18" height="6" fill="#fff"/><rect x="5" y="19" width="18" height="6" fill="#fff"/><rect x="20" y="20" width="10" height="9" rx="1" fill="#fff" stroke="#1b2f55" stroke-width="1.5"/></svg></div>
  <h3>Data Access<br>Filtering</h3>
  <p>Duis aute irure dolor in reprehenderit in voluptate</p>
</div>
<div class="card" style="left:850px">
  <div class="badge"><svg width="34" height="34" viewBox="0 0 34 34"><rect x="7" y="12" width="4" height="12" fill="#fff"/><rect x="13" y="7" width="4" height="17" fill="#fff"/><rect x="19" y="10" width="4" height="14" fill="#fff"/><rect x="25" y="14" width="4" height="10" fill="#fff"/><path d="M4 24c3 6 23 6 26 0" fill="none" stroke="#fff" stroke-width="2.5"/></svg></div>
  <h3>Infrastructure<br>Compliance</h3>
  <p>Duis aute irure dolor in reprehenderit in voluptate</p>
</div>

<h2 class="heading" style="top:1942px">Built on <b>ClearRule Keeper</b></h2>
<div class="rule" style="left:560px;top:2000px"></div>
<div class="partner" style="left:69px">Okvale</div>
<div class="partner" style="left:350px">Technora</div>
<div class="partner" style="left:617px">Commlink</div>
<div class="partner" style="left:905px">Techspire</div>

<h2 class="abs" style="left:113px;top:2270px;font-size:43px">Key <b style="color:var(--navy)">Features</b></h2>
<div class="rule" style="left:113px;top:2334px"></div>
<p class="feat" style="top:2363px">Each one only gets access to what it actually needs.</p>
<p class="feat" style="top:2419px">That access follows company rules automatically.</p>
<p class="feat" style="top:2475px">Those rules are enforced the same way everywhere — across apps, servers, and even AI tools.</p>
<div class="photo" role="img" aria-label="Blue network of connected nodes with security and AI icons" style="left:650px;top:2274px;width:433px;height:279px;border-top-left-radius:120px;background:radial-gradient(circle at 45% 45%,#2a6cc8,#0f2f6e 55%,#071838)"></div>

<section class="band" style="top:2680px;height:559px"></section>
<h2 class="heading" style="top:2732px">BrimCore <b>Capabilities</b></h2>
<div class="rule" style="left:560px;top:2794px"></div>
<div class="abs" style="left:500px;top:2920px;width:200px;text-align:center;font-size:30px;font-weight:900;color:var(--navy)">BRIMCORE</div>

<div class="cap-ic l" style="left:297px;top:2838px"><svg width="34" height="34" viewBox="0 0 34 34"><path d="M4 12L17 5l13 7z" fill="#fff"/><rect x="7" y="14" width="3" height="11" fill="#fff"/><rect x="13" y="14" width="3" height="11" fill="#fff"/><rect x="19" y="14" width="3" height="11" fill="#fff"/><rect x="25" y="14" width="3" height="11" fill="#fff"/><rect x="4" y="26" width="26" height="3" fill="#fff"/></svg></div>
<div class="cap-label" style="right:931px;top:2853px">Governance</div>
<div class="cap-ic l" style="left:348px;top:2931px"><svg width="32" height="32" viewBox="0 0 32 32"><rect x="4" y="4" width="11" height="14" rx="1" fill="#fff"/><rect x="17" y="4" width="11" height="9" rx="1" fill="#fff"/><rect x="4" y="20" width="11" height="8" rx="1" fill="#fff"/><rect x="17" y="15" width="11" height="13" rx="1" fill="#fff"/></svg></div>
<div class="cap-label" style="right:886px;top:2964px">Dashboard</div>
<div class="cap-ic l" style="left:420px;top:3007px"><svg width="34" height="34" viewBox="0 0 34 34"><circle cx="13" cy="10" r="6" fill="#fff"/><path d="M2 29c0-8 5-12 11-12 3 0 5 1 7 2v10z" fill="#fff"/><circle cx="25" cy="24" r="6" fill="#fff"/><circle cx="25" cy="24" r="2.5" fill="#1b2f55"/></svg></div>
<div class="cap-label" style="right:798px;top:3042px">Admin Assistant</div>
<div class="cap-ic l" style="left:505px;top:3085px"><svg width="34" height="34" viewBox="0 0 34 34"><circle cx="14" cy="14" r="9" fill="none" stroke="#fff" stroke-width="3"/><path d="M21 21l9 9" stroke="#fff" stroke-width="4"/></svg></div>
<div class="cap-label" style="right:709px;top:3118px">Threat Detection</div>

<div class="cap-ic r" style="left:866px;top:2843px"><svg width="30" height="30" viewBox="0 0 30 30"><path d="M7 3h11l6 6v18H7z" fill="#fff"/><rect x="11" y="14" width="9" height="2" fill="#e06c25"/><rect x="11" y="19" width="9" height="2" fill="#e06c25"/></svg></div>
<div class="cap-label" style="left:962px;top:2874px">Documentation</div>
<div class="cap-ic r" style="left:805px;top:2928px"><svg width="32" height="32" viewBox="0 0 32 32"><circle cx="9" cy="9" r="4" fill="#fff"/><circle cx="23" cy="9" r="4" fill="#fff"/><path d="M9 13v6c0 5 14 5 14 0v-6" fill="none" stroke="#fff" stroke-width="3"/></svg></div>
<div class="cap-label" style="left:889px;top:2959px">User Journey Generation</div>
<div class="cap-ic r" style="left:720px;top:3007px"><svg width="32" height="32" viewBox="0 0 32 32"><circle cx="9" cy="8" r="4" fill="#fff"/><circle cx="23" cy="24" r="4" fill="#fff"/><path d="M9 12v4h14v4" fill="none" stroke="#fff" stroke-width="3"/></svg></div>
<div class="cap-label" style="left:809px;top:3040px">User Journey Assistant</div>
<div class="cap-ic r" style="left:625px;top:3085px"><svg width="34" height="34" viewBox="0 0 34 34"><circle cx="17" cy="17" r="11" fill="none" stroke="#fff" stroke-width="4" stroke-dasharray="5 3"/><circle cx="17" cy="17" r="5" fill="#fff"/></svg></div>
<div class="cap-label" style="left:714px;top:3126px">Application Integration</div>

<h2 class="heading" style="top:3312px">Featured <b>Resources</b></h2>
<div class="rule" style="left:560px;top:3374px"></div>

<article class="post" style="left:113px">
  <div class="thumb" role="img" aria-label="Hand touching a glowing fingerprint scan interface"></div>
  <div class="tag">News</div>
  <h4>Why Access Control Needs a Rethink in the Age of AI”</h4>
  <div class="meta"><span>▦ Sep 29 ,2025</span><span>▭ 4 Comments</span></div>
</article>
<article class="post" style="left:444px">
  <div class="thumb" role="img" aria-label="Glowing code symbol above a laptop keyboard"></div>
  <div class="tag">News</div>
  <h4>From Permissions to Policies: The Next Evolution in Authorization</h4>
  <div class="meta"><span>▦ Sep 29 ,2025</span><span>▭ 4 Comments</span></div>
</article>
<article class="post" style="left:774px">
  <div class="thumb" role="img" aria-label="AI chip on a circuit board with streams of colored light"></div>
  <div class="tag">News</div>
  <h4>Containing AI: How to Stop LLMs from Leaking Sensitive Data</h4>
  <div class="meta"><span>▦ Sep 29 ,2025</span><span>▭ 4 Comments</span></div>
</article>
<a class="btn abs" style="left:530px;top:3830px;width:140px;height:49px;font-weight:400">VIEW ALL</a>

<footer class="footer"></footer>
<div class="f-head" style="left:118px;top:4057px">Quick Links</div>
<a class="f-link" style="top:4103px">Home</a>
<a class="f-link" style="top:4137px">Product</a>
<a class="f-link" style="top:4171px">Solutions</a>
<a class="f-link" style="top:4205px">Resources</a>
<a class="f-link" style="top:4239px">Company</a>
<a class="f-link" style="top:4273px">Contact Us</a>

<div class="f-brand">BRIMCORE</div>
<span class="social on" style="left:514px"></span>
<span class="social" style="left:548px"></span>
<span class="social" style="left:582px"></span>
<span class="social" style="left:616px"></span>
<span class="social" style="left:653px"></span>

<div class="f-head" style="left:873px;top:4057px">Contact Info</div>
<svg class="abs" style="left:870px;top:4112px" width="22" height="22" viewBox="0 0 22 22"><circle cx="11" cy="11" r="11" fill="#fff"/><path d="M11 4a5 5 0 00-5 5c0 4 5 9 5 9s5-5 5-9a5 5 0 00-5-5z" fill="#152a4f"/><circle cx="11" cy="9" r="2" fill="#fff"/></svg>
<div class="f-contact" style="top:4114px">Lorem Ipsum,USA -437916</div>
<svg class="abs" style="left:870px;top:4186px" width="22" height="22" viewBox="0 0 22 22"><circle cx="11" cy="11" r="11" fill="#fff"/><path d="M7 5l3 3-1.5 2c1 2 2.5 3.5 4.5 4.5L15 13l3 3-2 2C10 17 5 12 4 7z" fill="#152a4f"/></svg>
<div class="f-contact" style="top:4188px">+1 888 888 8888</div>
<svg class="abs" style="left:870px;top:4247px" width="22" height="22" viewBox="0 0 22 22"><circle cx="11" cy="11" r="11" fill="#fff"/><rect x="5" y="7" width="12" height="9" fill="#152a4f"/><path d="M5 7l6 5 6-5" fill="none" stroke="#fff" stroke-width="1.2"/></svg>
<div class="f-contact" style="top:4249px">info@brimcore.example</div>

<div class="f-rule"></div>
<div class="copy">© 2025 BrimCore.All rights reserved</div>

</body>
</html>
```